Business Card for Kinesiologist Practitioner

I need a logo and business card designing for a Kinesiologist Practitioner. I would like the card to be double sided. The look and feel of the logo and graphics should depict natural healing and well being. I would like a modern, fresh and contemporary design with a professional style. I have attached some logos and business cards that I liek from other natural health practitioners. I have also attached some logos that I like and a mock up of the business card style. Please however use your own creative input to change any element as you feel appropriate.

I have used the strap line "Quiet Meadow Care" which I would like underneath the logo. For the logo I like natural objects and possibly with 3 elements in the design as the course I have studied follows a "Lumora " healing concept (mind, body, soul). Maybe a tree or flower with 3 elements and a representation or suggestion of the human body somehow. You will see from the logos i have uploaded

Industry/Entity Type

Business

Contact Information for Business Card

Please see the mock up attached.

Font styles to use
Serif
Sans Serif

Colors
faa54b
acd036
fbee3d
85cae6

Requirements
Must have
• Note the colours are just suggested colours. Please us your own creative licence.

```html
<!DOCTYPE html>
<html lang="en">
<head>
<meta charset="utf-8">
<title>Quiet Meadow Care – Business Card</title>
<link rel="stylesheet" href="https://fonts.googleapis.com/css2?family=Cinzel:wght@400&family=Ubuntu:wght@400&family=Source+Sans+3:wght@400&display=swap">
<style>
  :root {
    --stage: #5e3d41;
    --card: #ffffff;
    --leaf-green: #acd036;
    --petal-orange: #faa54b;
    --ink: #4a4a4a;
    --ink-dark: #3a3a3a;
  }
  * { margin: 0; padding: 0; box-sizing: border-box; }
  html, body {
    width: 1200px;
    height: 1200px;
    overflow: hidden;
    background: var(--stage);
  }
  .card {
    position: absolute;
    left: 169px;
    width: 861px;
    height: 490px;
    background: var(--card);
    box-shadow: 0 3px 8px rgba(0,0,0,0.35);
  }
  .card--front { top: 74px; }
  .card--back  { top: 636px; }

  .brand-mark {
    position: absolute;
    border-radius: 50%;
    background: var(--petal-orange);
  }
  .brand-name {
    position: absolute;
    font-family: "Ubuntu", sans-serif;
    font-weight: 400;
    color: var(--leaf-green);
    white-space: nowrap;
    transform: translateX(-50%);
  }

  .card--front .brand-mark { width: 120px; height: 120px; left: 159px; top: 105px; }
  .card--front .brand-name { left: 219px; top: 292px; font-size: 36px; }

  .divider {
    position: absolute;
    left: 417px;
    top: 72px;
    width: 2px;
    height: 348px;
    background: var(--leaf-green);
  }

  .details {
    position: absolute;
    left: 419px;
    right: 0;
    top: 0;
    text-align: center;
  }
  .details__name {
    position: absolute;
    left: 0; right: 0;
    top: 144px;
    font-family: "Cinzel", serif;
    font-size: 36px;
    color: var(--ink-dark);
    letter-spacing: 0.5px;
  }
  .details__name .post-nominals { font-size: 25px; }
  .details__role {
    position: absolute;
    left: 0; right: 0;
    top: 187px;
    font-family: "Source Sans 3", sans-serif;
    font-size: 21px;
    color: var(--leaf-green);
  }
  .details__icons {
    position: absolute;
    left: 0; right: 0;
    top: 275px;
    display: flex;
    justify-content: center;
    gap: 12px;
  }
  .details__contact {
    position: absolute;
    left: 0; right: 0;
    top: 311px;
    font-family: "Source Sans 3", sans-serif;
    font-size: 22px;
    line-height: 29px;
    color: var(--ink);
  }

  .card--back .brand-mark { width: 190px; height: 190px; left: 336px; top: 90px; }
  .card--back .brand-name { left: 431px; top: 312px; font-size: 56px; }
</style>
</head>
<body>
  <section class="card card--front">
    <div class="brand-mark"></div>
    <div class="brand-name">Quiet Meadow Care</div>
    <div class="divider"></div>
    <div class="details">
      <div class="details__name">Clara Benning <span class="post-nominals">Dep, Cert.</span></div>
      <div class="details__role">Kinesiologist</div>
      <div class="details__icons">
        <svg class="icon icon--phone" width="20" height="26" viewBox="0 0 20 26" aria-label="Phone">
          <rect x="2" y="1" width="16" height="24" rx="2.5" fill="none" stroke="var(--leaf-green)" stroke-width="2.4"/>
          <line x1="3" y1="19" x2="17" y2="19" stroke="var(--leaf-green)" stroke-width="2"/>
          <circle cx="10" cy="22" r="1.2" fill="var(--leaf-green)"/>
        </svg>
        <svg class="icon icon--mail" width="26" height="20" viewBox="0 0 26 20" aria-label="Email">
          <rect x="1" y="2" width="24" height="16" fill="var(--leaf-green)"/>
          <polyline points="3,4 13,12 23,4" fill="none" stroke="#fff" stroke-width="1.6"/>
          <line x1="3" y1="16" x2="10" y2="10" stroke="#fff" stroke-width="1.4"/>
          <line x1="23" y1="16" x2="16" y2="10" stroke="#fff" stroke-width="1.4"/>
        </svg>
      </div>
      <div class="details__contact">
        <div class="details__phone">0400 555 012</div>
        <div class="details__email">clarabenning@meadowmail.com</div>
      </div>
    </div>
  </section>

  <section class="card card--back">
    <div class="brand-mark"></div>
    <div class="brand-name">Quiet Meadow Care</div>
  </section>
</body>
</html>
```